Handyman home maintenance postcard

We would like the postcard to state what we do : Painting, plumbing, electrical, flooring, carpentry, drywall, fencing, windows and more. We would also like our promotion to state : First four hours of work is only $299. Additional hours are 25% off our regular rate of $110 an hour. Rate includes two expert handymen working to complete your job.

Target Market(s)

30-75

Industry/Entity Type

Home maintenance

```html
<!DOCTYPE html>
<html lang="en">
<head>
<meta charset="utf-8">
<title>Keystone Handyman Services – Postcard</title>
<link href="https://fonts.googleapis.com/css2?family=Poppins:wght@400;500;600;700;800&display=swap" rel="stylesheet">
<style>
  :root{
    --orange:#f7941d;
    --orange-deep:#f26a1b;
    --orange-light:#fbb03b;
    --ink:#333333;
    --ink-soft:#2b2b2b;
    --white:#ffffff;
    --paper:#f4f4f4;
    --stage:#7f7f7f;
    --rule:#d8d8d8;
  }
  *{box-sizing:border-box;margin:0;padding:0}
  html,body{width:728px;height:1200px;overflow:hidden;background:var(--stage)}
  body{font-family:"Poppins",sans-serif;color:var(--ink)}
  .canvas{position:relative;width:728px;height:1200px;overflow:hidden;background:var(--stage)}
  .postcard{position:absolute;left:24px;width:680px;height:453px;background:var(--white);overflow:hidden}
  .postcard--front{top:127px}
  .postcard--back{top:620px}

  /* ---------- front ---------- */
  .brand{position:absolute;left:28px;top:40px;display:flex;align-items:center;gap:10px}
  .brand__dot{width:24px;height:24px;border-radius:50%;background:var(--orange)}
  .brand__name{font-weight:700;font-size:19px;color:var(--ink);font-family:"Poppins",sans-serif}
  .estimate{position:absolute;left:0;width:399px;top:98px;text-align:center;font-size:11px;font-weight:500}
  .phone-big{position:absolute;left:0;width:399px;top:112px;display:flex;justify-content:center;align-items:center;gap:10px}
  .phone-big__icon{width:20px;height:20px}
  .phone-big__num{font-size:33px;font-weight:700;color:var(--orange);letter-spacing:.5px}
  .crew-photo{position:absolute;left:0;top:162px;width:399px;height:291px;
    background:linear-gradient(180deg,#f6f6f8 0%,#dfe3ee 55%,#3c4fa6 100%)}

  .headline-panel{position:absolute;left:360px;top:0;width:320px;height:188px;
    background:linear-gradient(120deg,var(--orange-light) 0%,var(--orange) 45%,var(--orange-deep) 100%);
    border-bottom-left-radius:14px}
  .headline-tail{position:absolute;left:360px;top:182px;width:50px;height:26px}
  .headline{position:absolute;left:22px;top:22px;font-size:34px;line-height:35px;font-weight:800;color:var(--white);text-transform:uppercase}
  .headline__sub{position:absolute;left:22px;top:133px;font-size:14px;line-height:18px;color:var(--white)}
  .mascot{position:absolute;left:234px;top:92px;width:72px;height:88px;border-radius:12px;background:#b9b9bd}

  .offer-panel{position:absolute;left:399px;top:191px;width:281px;height:262px;background:var(--ink);
    clip-path:polygon(0 10px,20px 0,100% 0,100% 100%,0 100%)}
  .offer__lead{position:absolute;left:26px;top:34px;font-size:14.5px;line-height:16.5px;color:var(--white)}
  .offer__only{position:absolute;left:199px;top:16px;background:var(--white);color:var(--ink);font-size:10px;font-weight:700;padding:0 6px;border-radius:8px;line-height:13px}
  .offer__price{position:absolute;left:106px;top:18px;font-size:62px;line-height:70px;font-weight:800;color:var(--orange);letter-spacing:-1px}
  .offer__limited{position:absolute;right:28px;top:88px;font-size:10px;color:var(--white)}
  .rate-box{position:absolute;left:26px;top:112px;width:229px;height:94px;border:3px solid var(--white);background:var(--white)}
  .rate-box__top{height:48px;background:var(--orange);display:flex;align-items:center;padding:0 10px;gap:12px}
  .rate-box__label{font-size:13px;line-height:13px;color:var(--white)}
  .rate-box__deal{font-size:29px;font-weight:800;color:var(--white)}
  .rate-box__bottom{display:flex;align-items:center;padding:4px 10px;gap:8px}
  .rate-box__regular{font-size:13px;line-height:14px}
  .rate-box__amount{font-size:30px;font-weight:800;color:var(--ink-soft)}
  .rate-box__unit{font-size:12px}
  .offer__note{position:absolute;left:0;width:281px;top:213px;text-align:center;font-size:12.5px;line-height:16px;color:var(--white)}

  /* ---------- back ---------- */
  .sweep{position:absolute;left:0;top:0;width:680px;height:453px}
  .back-title{position:absolute;left:30px;top:20px;font-size:23px;line-height:26px;font-weight:800;color:var(--white);text-transform:uppercase}
  .services-bar{position:absolute;left:30px;top:83px;width:220px;height:36px;background:var(--ink);color:var(--white);
    font-size:22px;font-weight:700;display:flex;align-items:center;justify-content:center}
  .services{position:absolute;left:28px;top:132px;width:300px;display:grid;grid-template-columns:130px 140px;row-gap:11px;column-gap:0}
  .service{display:flex;align-items:center;gap:12px;font-size:14.5px;font-weight:600;color:var(--white);min-height:25px;line-height:15px}
  .service svg{width:26px;height:26px;flex:none}
  .contact-box{position:absolute;left:26px;top:366px;width:230px;height:75px;background:var(--white);padding:3px}
  .contact-box__phone{height:40px;background:var(--ink);display:flex;align-items:center;justify-content:center;gap:6px}
  .contact-box__phone span{font-size:26px;font-weight:700;color:var(--orange)}
  .contact-box__web{display:flex;align-items:center;justify-content:center;gap:5px;font-size:11.5px;font-weight:500;margin-top:6px}
  .contact-box__web i{width:9px;height:9px;border-radius:50%;background:var(--orange);display:block}
  .job-photo{position:absolute;border-radius:50%;border:4px solid var(--white)}
  .job-photo--meter{left:316px;top:83px;width:126px;height:126px;background:radial-gradient(circle at 40% 40%,#e9e4dc,#8d8a86)}
  .job-photo--drill{left:312px;top:197px;width:124px;height:124px;background:radial-gradient(circle at 55% 60%,#f4c145,#8a6a4a)}
  .mascot--back{position:absolute;left:476px;top:26px;width:66px;height:82px;border-radius:12px;background:#b9b9bd}
  .stamp{position:absolute;left:604px;top:26px;width:60px;height:60px;background:#dcdcdc}
  .address-line{position:absolute;left:466px;width:198px;height:1px;background:var(--rule)}
  .quote-mark{position:absolute;left:404px;top:332px;font-size:40px;font-weight:800;color:#b0b0b0;line-height:40px}
  .testimonial{position:absolute;left:446px;top:298px;width:222px;font-size:9.8px;line-height:12.6px;color:var(--ink)}
  .reviewer{position:absolute;left:446px;top:405px;font-size:12px;font-weight:700}
  .stars{position:absolute;left:565px;top:402px;font-size:13px;letter-spacing:5px;color:var(--orange)}
</style>
</head>
<body>
<div class="canvas">

  <!-- FRONT -->
  <section class="postcard postcard--front">
    <div class="brand"><span class="brand__dot"></span><span class="brand__name">Keystone Handyman Services</span></div>
    <p class="estimate">Call Us for a Free Estimate</p>
    <div class="phone-big">
      <svg class="phone-big__icon" viewBox="0 0 20 20"><circle cx="10" cy="10" r="10" fill="#333"/><path d="M7 5c.6-.3 1.1 0 1.4.6l.7 1.5c.2.5 0 .9-.4 1.2l-.6.4c.5 1.2 1.4 2.1 2.6 2.6l.4-.6c.3-.4.8-.6 1.2-.4l1.5.7c.6.3.9.8.6 1.4-.4 1-1.4 1.7-2.6 1.4C9 13.3 6.7 11 6.2 8c-.2-1.2.1-2.3.8-3z" fill="#fff"/></svg>
      <span class="phone-big__num">310 555 0148</span>
    </div>
    <div class="crew-photo" role="img" aria-label="Photo of three smiling handymen in blue overalls, tool belts and work gloves"></div>

    <div class="headline-panel">
      <h1 class="headline">Your Local<br>Trusted<br>Handymen</h1>
      <p class="headline__sub">20+ years of experience<br>serving Los Angeles</p>
      <div class="mascot" role="img" aria-label="Cartoon cat mascot wearing an orange hard hat and holding a hammer"></div>
    </div>
    <svg class="headline-tail" viewBox="0 0 50 26"><path d="M0 0H50L14 24Z" fill="#f58220"/></svg>

    <div class="offer-panel">
      <p class="offer__lead">First four<br>hours of<br>work is</p>
      <span class="offer__only">ONLY</span>
      <p class="offer__price">$299</p>
      <p class="offer__limited">For a limited time</p>
      <div class="rate-box">
        <div class="rate-box__top"><span class="rate-box__label">Additional<br>hours are</span><span class="rate-box__deal">25% off</span></div>
        <div class="rate-box__bottom"><span class="rate-box__regular">our regular<br>rate of</span><span class="rate-box__amount">$110</span><span class="rate-box__unit">an hour.</span></div>
      </div>
      <p class="offer__note">Rate includes two expert handymen<br>working to complete your job.</p>
    </div>
  </section>

  <!-- BACK -->
  <section class="postcard postcard--back">
    <svg class="sweep" viewBox="0 0 680 453" preserveAspectRatio="none">
      <defs>
        <linearGradient id="sweepFill" x1="0" y1="0" x2="1" y2="1">
          <stop offset="0" stop-color="#f26a1b"/>
          <stop offset=".6" stop-color="#f7941d"/>
          <stop offset="1" stop-color="#fbb03b"/>
        </linearGradient>
      </defs>
      <path d="M0 0H376C420 120 460 330 580 453H0Z" fill="url(#sweepFill)"/>
      <path d="M368 0H386C404 50 414 110 420 160C410 110 392 50 368 0Z" fill="#333"/>
    </svg>

    <h2 class="back-title">Your Expert Go-To<br>For Home Repairs</h2>
    <div class="services-bar">SERVICES</div>

    <ul class="services">
      <li class="service"><svg viewBox="0 0 26 26" fill="none" stroke="#222" stroke-width="1.6"><rect x="2" y="16" width="22" height="6"/><path d="M4 4l12 10M4 4l3-2 12 10"/></svg>Carpentry</li>
      <li class="service"><svg viewBox="0 0 26 26" fill="none" stroke="#222" stroke-width="1.6"><path d="M3 22h20l-3-7H6z"/><path d="M8 4l8 9"/></svg>Concrete</li>
      <li class="service"><svg viewBox="0 0 26 26" fill="none" stroke="#222" stroke-width="1.6"><path d="M3 23V7l2-3 2 3v16M10 23V7l2-3 2 3v16M17 23V7l2-3 2 3v16M2 11h22M2 18h22"/></svg>Fencing</li>
      <li class="service"><svg viewBox="0 0 26 26" fill="none" stroke="#222" stroke-width="1.6"><circle cx="13" cy="13" r="10"/><path d="M10 7v5M16 7v5M8 12h10v3a5 5 0 0 1-10 0z"/></svg>Electrical</li>
      <li class="service"><svg viewBox="0 0 26 26" fill="none" stroke="#222" stroke-width="1.6"><path d="M8 3h10M9 3v4l4 3 4-3V3M13 10v13M9 14h8M9 18h8"/></svg>Drywall</li>
      <li class="service"><svg viewBox="0 0 26 26" fill="none" stroke="#222" stroke-width="1.6"><path d="M4 4l18 18M22 4L4 22"/><circle cx="5" cy="5" r="2"/><circle cx="21" cy="5" r="2"/></svg>Maintenance</li>
      <li class="service"><svg viewBox="0 0 26 26" fill="none" stroke="#222" stroke-width="1.6"><rect x="3" y="3" width="16" height="7" rx="1"/><path d="M19 6h3v7h-9v4M11 17h4v6h-4z"/></svg>Painting</li>
      <li class="service"><svg viewBox="0 0 26 26" fill="none" stroke="#222" stroke-width="1.6"><path d="M13 4l10 6-10 6-10-6zM3 14l10 6 10-6M3 18l10 6 10-6"/></svg>Tile</li>
      <li class="service"><svg viewBox="0 0 26 26" fill="none" stroke="#222" stroke-width="1.6"><path d="M5 3v20M10 3v15a3 3 0 0 0 6 0v-6h6M5 3h5M16 9h6"/></svg>Plumbing</li>
      <li class="service"><svg viewBox="0 0 26 26" fill="none" stroke="#222" stroke-width="1.6"><rect x="4" y="3" width="18" height="20"/><path d="M13 3v20M4 13h18"/></svg>Windows/<br>Doors</li>
      <li class="service"><svg viewBox="0 0 26 26" fill="none" stroke="#222" stroke-width="1.6"><rect x="3" y="3" width="20" height="20"/><path d="M3 10L10 3M3 17L17 3M3 23L23 3M10 23L23 10M17 23l6-6"/></svg>Flooring</li>
    </ul>

    <div class="contact-box">
      <div class="contact-box__phone">
        <svg width="16" height="16" viewBox="0 0 20 20"><circle cx="10" cy="10" r="10" fill="#f7941d"/><path d="M7 5c.6-.3 1.1 0 1.4.6l.7 1.5c.2.5 0 .9-.4 1.2l-.6.4c.5 1.2 1.4 2.1 2.6 2.6l.4-.6c.3-.4.8-.6 1.2-.4l1.5.7c.6.3.9.8.6 1.4-.4 1-1.4 1.7-2.6 1.4C9 13.3 6.7 11 6.2 8c-.2-1.2.1-2.3.8-3z" fill="#333"/></svg>
        <span>310 555 0148</span>
      </div>
      <p class="contact-box__web"><i></i>keystonehandypros.com</p>
    </div>

    <div class="job-photo job-photo--meter" role="img" aria-label="Photo of an electrician testing a breaker panel with a multimeter"></div>
    <div class="job-photo job-photo--drill" role="img" aria-label="Photo of a hand using a yellow cordless drill on cabinet hardware"></div>

    <div class="mascot--back" role="img" aria-label="Cartoon cat mascot wearing an orange hard hat and holding a hammer"></div>
    <div class="stamp"></div>
    <div class="address-line" style="top:149px"></div>
    <div class="address-line" style="top:205px"></div>
    <div class="address-line" style="top:261px"></div>

    <span class="quote-mark">&ldquo;</span>
    <p class="testimonial">I hired them after a coworker used them and recommended them to me. She could not say enough good things about them. So i decided to give them a try. From the first call to a finished job it was the most professional business ive done business with in a long time. They were on time and worked perfectly with our crazy schedule days</p>
    <p class="reviewer">- Marla Jennings</p>
    <p class="stars">★★★★★</p>
  </section>

</div>
</body>
</html>
```